Hvac and insulation company needs good looking business card design

We are hvac and insulation company and looking for a new business cards that look to today standards designs

Target Market(s)

homeowners

Industry/Entity Type

Hvac

Contact Information for Business Card

Name: Dorian Velkova
Home comfort consultant
address: 4827 Marrow Ridge Rd #215 Larkvale, CA 95318
office: 888-317-5069
cell: 510-642-1388
Lic.# 458127
Email: dorian@quarry-hvac.com
Web: quarry-hvac.com

Requirements
Must have
• clean and sleek look
Nice to have
• simple with a clean look
Should not have
• to busy business card

```html
<!DOCTYPE html>
<html lang="en">
<head>
<meta charset="utf-8">
<title>Quarry Home Solutions – Business Card</title>
<link rel="stylesheet" href="https://fonts.googleapis.com/css2?family=Roboto:wght@400;500;700&display=swap">
<style>
  :root {
    --bg: #1d1d1d;
    --white: #ffffff;
    --orange: #ec741c;
    --orange-deep: #e6610f;
    --grey: #767370;
    --grey-top: #75716d;
    --grey-bottom: #66615e;
    --divider: #e4e4e4;
    --text-grey: #555555;
  }
  * { box-sizing: border-box; margin: 0; padding: 0; }
  html, body {
    width: 1200px; height: 1001px; overflow: hidden;
    background: var(--bg);
    font-family: "Roboto", Arial, sans-serif;
  }
  .canvas { position: relative; width: 1200px; height: 1001px; }
  .card {
    position: absolute; left: 306px; width: 589px; height: 330px; overflow: hidden;
  }
  .card-front { top: 134px; background: var(--white); }
  .card-back {
    top: 538px;
    background: linear-gradient(to bottom, var(--grey-top), var(--grey-bottom) 90%);
  }

  /* front */
  .identity { position: absolute; left: 34px; top: 67px; }
  .identity-name {
    color: var(--orange); font-weight: 700; font-size: 19px; letter-spacing: -0.2px;
    line-height: 1;
  }
  .identity-title { color: var(--text-grey); font-size: 13.5px; margin-top: 5px; }

  .brand { position: absolute; display: flex; align-items: center; color: var(--orange); }
  .brand-mark { background: var(--orange); flex: none; }
  .brand-name { font-weight: 500; line-height: 1; letter-spacing: -0.3px; white-space: nowrap; }

  .brand-front { right: 34px; top: 67px; gap: 9px; }
  .brand-front .brand-mark { width: 32px; height: 32px; }
  .brand-front .brand-name { font-size: 24px; }

  .divider { position: absolute; left: 0; top: 163px; width: 100%; height: 7px; background: var(--divider); }
  .contact-band { position: absolute; left: 0; top: 170px; width: 100%; height: 130px; background: var(--orange); }
  .notch { position: absolute; left: 34px; top: 170px; }
  .footer-band { position: absolute; left: 0; top: 300px; width: 100%; height: 30px; background: var(--grey); }

  .contact-list {
    position: absolute; left: 36px; top: 34px; list-style: none;
    color: var(--white); font-size: 13.5px;
  }
  .contact-list li { display: flex; align-items: center; height: 17.5px; }
  .contact-list svg { width: 13px; height: 13px; margin-right: 9px; flex: none; }

  .address {
    position: absolute; right: 34px; top: 34px; text-align: right;
    color: var(--white); font-size: 13.5px; line-height: 17px;
  }
  .license { margin-top: 16px; }

  /* back */
  .brand-back { left: 50%; top: 138px; transform: translateX(-50%); gap: 12px; }
  .brand-back .brand-mark { width: 48px; height: 48px; }
  .brand-back .brand-name { font-size: 32px; }
  .back-band { position: absolute; left: 0; top: 299px; width: 100%; height: 31px; background: var(--orange-deep); }
</style>
</head>
<body>
<main class="canvas">

  <section class="card card-front" aria-label="Business card front">
    <div class="identity">
      <p class="identity-name">DORIAN VELKOVA</p>
      <p class="identity-title">Home comfort consultant</p>
    </div>

    <div class="brand brand-front">
      <span class="brand-mark"></span>
      <span class="brand-name">quarry home solutions</span>
    </div>

    <div class="divider"></div>
    <div class="contact-band">
      <ul class="contact-list">
        <li>
          <svg viewBox="0 0 14 14" aria-hidden="true"><rect x="3.5" y="0.8" width="7" height="12.4" rx="1.4" fill="none" stroke="#fff" stroke-width="1.6"/><rect x="5.5" y="10" width="3" height="1.2" fill="#fff"/></svg>
          510-642-1388
        </li>
        <li>
          <svg viewBox="0 0 14 14" aria-hidden="true"><path d="M4 1 L6 4.5 L4.6 6 Q5.6 8.6 8 9.6 L9.5 8.2 L13 10.2 L11.6 13 Q6 13 2.6 8.4 Q0.8 5 2 2 Z" fill="#fff"/></svg>
          888-317-5069
        </li>
        <li>
          <svg viewBox="0 0 14 14" aria-hidden="true"><rect x="0.8" y="3" width="12.4" height="8.5" fill="#fff"/><path d="M1 3.2 L7 8 L13 3.2" fill="none" stroke="#ec741c" stroke-width="1.1"/></svg>
          dorian@quarry-hvac.com
        </li>
        <li>
          <svg viewBox="0 0 14 14" aria-hidden="true"><g fill="none" stroke="#fff" stroke-width="1"><circle cx="7" cy="7" r="6"/><ellipse cx="7" cy="7" rx="2.6" ry="6"/><path d="M1 7 H13 M2 4 H12 M2 10 H12"/></g></svg>
          www.quarry-hvac.com
        </li>
      </ul>
      <div class="address">
        <p>4827 Marrow Ridge Rd #215</p>
        <p>Larkvale, CA 95318</p>
        <p class="license">Lic.# 458127</p>
      </div>
    </div>
    <svg class="notch" width="20" height="10" viewBox="0 0 20 10" aria-hidden="true"><path d="M0 0 H20 L10 10 Z" fill="#ffffff"/></svg>
    <div class="footer-band"></div>
  </section>

  <section class="card card-back" aria-label="Business card back">
    <div class="brand brand-back">
      <span class="brand-mark"></span>
      <span class="brand-name">quarry home solutions</span>
    </div>
    <div class="back-band"></div>
  </section>

</main>
</body>
</html>
```